Pine Hollow Camp Brochure Design - TRI FOLD - See text examples added

Tri- Fold Brochure designed for Remote Alaskan Wilderness Fly-in lodge.We will provide several pictures. We want activities, directions, lodge rules, history, etc... We have provided our logo. Will work on adding text.
Looking for a professional, fun, adventurous feel.
Guests must fly in to the lodge. We are completely surrounded by wilderness. 33 miles from the nearest road. Take a 30 min flight seeing trip over mountains, glaciers, rivers and wildlife with Sky Tundrix to our private airstrip. Canoe in Heron Pond. See the Moose, Caribou, Bears, Lynx, wolves, and various birds. Go gold panning in the creeks.
Accommodations include your own private cabin with private bathroom. Access to the main lodge lounge and dining rooms, wood fired sauna, covered fire pit, and use of our canoe, life jackets, and rubber boots. Meals available. Wifi in main lodge. Movies in Theater.

Target Market(s)

Adventure, photographers, hikers, mountaineers, travelers

Industry/Entity Type

Tourism

Requirements
Must have
• Logo and pictures, information - Tri-Fold
Nice to have
• High quality attractive design with logo and information
Should not have
• Cartoony feel

```html
<!DOCTYPE html>
<html lang="en">
<head>
<meta charset="utf-8">
<title>Pine Hollow Camp — Brochure Covers</title>
<link href="https://fonts.googleapis.com/css2?family=Cormorant+SC:wght@500;600&family=Dancing+Script:wght@500&display=swap" rel="stylesheet">
<style>
  :root {
    --stage: #e4e4e4;
    --orange: #e8561f;
    --orange-deep: #d9461a;
    --orange-soft: #f29a6b;
    --slate: #2a323e;
    --slate-light: #3b4553;
    --paper: #ffffff;
    --cream: #fbe3d4;
  }
  html, body {
    margin: 0;
    padding: 0;
    width: 1200px;
    height: 824px;
    overflow: hidden;
    background: var(--stage);
  }
  .spread {
    position: absolute;
    left: 180px;
    top: 115px;
    width: 840px;
    height: 594px;
    display: flex;
    box-shadow: 0 10px 30px rgba(0,0,0,0.18);
  }
  .page { width: 420px; height: 594px; display: block; }
  .serif { font-family: "Cormorant SC", "Times New Roman", serif; }
  .script { font-family: "Dancing Script", cursive; }
</style>
</head>
<body>
<main class="spread">

  <!-- Back cover -->
  <svg class="page back-cover" viewBox="0 0 420 594" xmlns="http://www.w3.org/2000/svg">
    <defs>
      <linearGradient id="lodgeScene" x1="0" y1="0" x2="0" y2="1">
        <stop offset="0" stop-color="#9fb8d4"/>
        <stop offset="0.35" stop-color="#c8d6e2"/>
        <stop offset="0.55" stop-color="#5d6b4a"/>
        <stop offset="0.8" stop-color="#2c2a22"/>
        <stop offset="1" stop-color="#4a4a3e"/>
      </linearGradient>
      <linearGradient id="orangeFade" x1="0" y1="0" x2="1" y2="1">
        <stop offset="0" stop-color="var(--orange)"/>
        <stop offset="1" stop-color="var(--orange-deep)"/>
      </linearGradient>
    </defs>
    <rect class="lodge-photo" x="0" y="0" width="420" height="360" fill="url(#lodgeScene)" role="img" aria-label="Log lodge among tall pines with a snow-capped mountain behind"/>
    <path class="band-dark" d="M0,330 C140,292 290,286 420,268 L420,594 L0,594 Z" fill="var(--slate)"/>
    <path class="band-orange" d="M0,372 C150,330 300,316 385,312 C340,420 330,520 362,594 L0,594 Z" fill="url(#orangeFade)"/>
    <path class="accent-line" d="M0,352 C150,312 300,300 420,286" fill="none" stroke="var(--paper)" stroke-width="1"/>

    <g class="testimonial">
      <text class="serif" x="18" y="412" font-size="40" fill="var(--orange-soft)">“</text>
      <text class="serif" x="360" y="388" font-size="40" fill="var(--orange-soft)">”</text>
      <text class="script" font-size="10.5" fill="var(--paper)">
        <tspan x="30" y="412">Lorem ipsum dolor sit amet, consectetur adipisicing elit, sed do</tspan>
        <tspan x="30" y="425">eiusmod tempor incididunt ut labore et dolore magna aliqua. Ut</tspan>
        <tspan x="30" y="438">enim ad minim veniam, quis nostrud exercitation ullamco laboris</tspan>
        <tspan x="30" y="451">nisi ut aliquip ex ea commodo consequat.</tspan>
      </text>
      <text class="serif" x="330" y="452" font-size="9" fill="var(--paper)" text-anchor="end" letter-spacing="0.5">LOREM IPSUM DOLOR</text>
    </g>

    <g class="contact">
      <text class="serif" x="30" y="505" font-size="17" fill="var(--paper)">CONTACT US</text>
      <path d="M30,512 L82,512 L70,518 Z" fill="var(--slate)"/>
      <line x1="40" y1="524" x2="40" y2="572" stroke="var(--slate)" stroke-width="1"/>
      <g fill="var(--slate)">
        <circle cx="40" cy="528" r="3"/>
        <circle cx="40" cy="543" r="3"/>
        <circle cx="40" cy="556" r="3"/>
        <circle cx="40" cy="569" r="3"/>
      </g>
      <text class="serif" font-size="8.5" fill="var(--cream)">
        <tspan x="50" y="526">Address Line 1, Address Line 1</tspan>
        <tspan x="50" y="535">Address Line 1</tspan>
        <tspan x="50" y="546">info@yourmail.com</tspan>
        <tspan x="50" y="559">0123 456 789</tspan>
        <tspan x="50" y="572">www.yourweburl.com</tspan>
      </text>
    </g>

    <g class="brand-mark">
      <circle cx="222" cy="487" r="5" fill="var(--slate)"/>
      <text class="serif" x="232" y="491" font-size="12" font-weight="600" fill="var(--paper)">Pine Hollow Camp</text>
    </g>
  </svg>

  <!-- Front cover -->
  <svg class="page front-cover" viewBox="0 0 420 594" xmlns="http://www.w3.org/2000/svg">
    <defs>
      <linearGradient id="lakeScene" x1="0" y1="0" x2="0" y2="1">
        <stop offset="0" stop-color="#7f93b4"/>
        <stop offset="0.22" stop-color="#d7dbe6"/>
        <stop offset="0.34" stop-color="#3d4a3a"/>
        <stop offset="0.46" stop-color="#b9b3c4"/>
        <stop offset="0.6" stop-color="#7a4a55"/>
        <stop offset="0.75" stop-color="#b6874f"/>
        <stop offset="1" stop-color="#6a5a3a"/>
      </linearGradient>
      <linearGradient id="planeScene" x1="0" y1="0" x2="0" y2="1">
        <stop offset="0" stop-color="#a9c3da"/>
        <stop offset="0.5" stop-color="#8aa3b5"/>
        <stop offset="1" stop-color="#5c5a56"/>
      </linearGradient>
      <linearGradient id="cabinScene" x1="0" y1="0" x2="0" y2="1">
        <stop offset="0" stop-color="#b9c7cf"/>
        <stop offset="0.5" stop-color="#5b4a3a"/>
        <stop offset="1" stop-color="#3a4a32"/>
      </linearGradient>
      <linearGradient id="guestScene" x1="0" y1="0" x2="0" y2="1">
        <stop offset="0" stop-color="#8fb0c8"/>
        <stop offset="0.5" stop-color="#c89a7c"/>
        <stop offset="1" stop-color="#3f7a6b"/>
      </linearGradient>
    </defs>
    <rect class="lake-photo" x="0" y="0" width="420" height="594" fill="url(#lakeScene)" role="img" aria-label="Mountain lake at dusk with autumn tundra and spruce trees"/>
    <path class="corner-orange" d="M0,0 L290,0 L200,62 Z" fill="var(--orange)"/>
    <path class="band-dark" d="M0,446 C110,418 260,392 420,372 L420,594 L0,594 Z" fill="var(--slate)"/>
    <path class="band-slate" d="M0,446 C25,440 48,436 72,431 C42,470 24,530 22,594 L0,594 Z" fill="var(--slate-light)"/>
    <path class="accent-line" d="M72,431 C42,470 24,530 22,594" fill="none" stroke="var(--paper)" stroke-width="1"/>

    <g class="photo-circles" stroke="var(--orange)" stroke-width="7">
      <circle cx="155" cy="385" r="78" fill="url(#planeScene)" role="img" aria-label="Float plane parked on a gravel airstrip"/>
      <circle cx="262" cy="305" r="60" fill="url(#cabinScene)" role="img" aria-label="Log cabin entrance with antlers above the door"/>
      <circle cx="258" cy="420" r="56" fill="url(#guestScene)" role="img" aria-label="Smiling family of guests by the lake"/>
    </g>

    <g class="brand-mark">
      <circle cx="232" cy="60" r="6" fill="var(--orange)"/>
      <text class="serif" x="244" y="65" font-size="16" font-weight="600" fill="var(--slate)">Pine Hollow Camp</text>
    </g>

    <text class="serif title" font-size="21" font-weight="600" fill="var(--paper)" text-anchor="middle" letter-spacing="0.5">
      <tspan x="245" y="506">REMOTE ALASKAN</tspan>
      <tspan x="245" y="530">WILDERNESS FLY-IN LODGE</tspan>
    </text>
    <rect class="url-bar" x="100" y="546" width="320" height="24" fill="var(--orange)"/>
    <text class="serif" x="260" y="562" font-size="9.5" fill="var(--cream)" text-anchor="middle" letter-spacing="1">WWW.YOURWEBURL.COM</text>
  </svg>

</main>
</body>
</html>
```